I need a cd cover my CD. The cd is about my journey in my recovery from addiction. The name of the CD is Garden of Silent Wells. I would like something artsy that reflects the song. The song is a metaphor so I am not looking for something where doors are the main emphasis for the cover. During my addiction I burned a lot of bridges, hurt a lot of people, hurt myself and my 3 1/2 year old son died in a house fire while I was sitting in a jail cell. So the garden of Silent Wells song is a battle that I have in my head... sometimes on a daily basis about picking up and using again. So I play the tape of my life in my head of all of the crap that I've created and what I've done. When I do that, it stops me from relapsing, because I know what will happen if I do.

I don't want a photo. I also want my name on the cd to be Owen T. Don't add my last name just the initial. I've attached the link to the song and also another song called Stay Near. Also that you can get a feel for it. Also disregard the image that's on ClipNest.

https://www.clipnest-video.example/play?v=qR7__mp_ZX3k&t=42s

https://www.clipnest-video.example/play?v=8TbwLa2Pqne

Target Market(s)

People in Recovery, Sobriety

Industry/Entity Type

Music Download

Font styles to use
Serif

Colors

Designer to choose colors to be used in the design.

Requirements
Must have
• A mysterious feel to it.
Nice to have
• The song is about my secret space which is actually inside my mind. It's a place I go to, kind of like a tape I play that in my head that if I relapse, This will happen and that will happen etc... I also want something that will look good on a T-Shirt and Hats etc...
Should not have
• Nothing Gothic and no Photographs.

```html
<!DOCTYPE html>
<html lang="en">
<head>
<meta charset="utf-8">
<title>Garden of Silent Wells — Owen T.</title>
<link rel="stylesheet" href="https://fonts.googleapis.com/css2?family=Montserrat:wght@400;600&display=swap">
<style>
  :root {
    --backdrop: #3c3c3c;
    --cover-dark: #0b0b0d;
    --cover-mid: #161a22;
    --cover-haze: #1f2633;
    --title-orange: #e07a1f;
    --artist-white: #f4f4f4;
  }
  html, body {
    margin: 0;
    padding: 0;
    width: 1200px;
    height: 960px;
    overflow: hidden;
    background: var(--backdrop);
  }
  .canvas {
    position: relative;
    width: 1200px;
    height: 960px;
  }
  .cover {
    position: absolute;
    left: 161px;
    top: 44px;
    width: 878px;
    height: 878px;
    overflow: hidden;
    background: var(--cover-dark);
  }
  .cover-texture {
    position: absolute;
    inset: 0;
    background:
      radial-gradient(ellipse 30% 18% at 52% 12%, rgba(40,50,68,0.55), transparent 70%),
      radial-gradient(ellipse 22% 28% at 88% 28%, rgba(34,42,58,0.45), transparent 70%),
      radial-gradient(ellipse 14% 14% at 20% 32%, rgba(44,54,72,0.5), transparent 70%),
      radial-gradient(ellipse 45% 35% at 80% 80%, rgba(30,37,50,0.55), transparent 70%),
      radial-gradient(ellipse 40% 30% at 15% 75%, rgba(20,24,32,0.5), transparent 70%),
      linear-gradient(160deg, var(--cover-mid), var(--cover-dark) 55%, #0d0f14);
  }
  .cover-type {
    position: absolute;
    left: 0;
    right: 0;
    top: 404px;
    text-align: center;
    font-family: "Montserrat", sans-serif;
  }
  .album-title {
    margin: 0;
    font-size: 27px;
    font-weight: 600;
    letter-spacing: 0.55em;
    padding-left: 0.55em;
    color: var(--title-orange);
    text-transform: uppercase;
    line-height: 1;
  }
  .artist-name {
    margin: 22px 0 0;
    font-size: 21px;
    font-weight: 400;
    letter-spacing: 0.6em;
    padding-left: 0.6em;
    color: var(--artist-white);
    text-transform: uppercase;
    line-height: 1;
  }
</style>
</head>
<body>
  <main class="canvas">
    <section class="cover">
      <div class="cover-texture" role="img" aria-label="Dark weathered plaster texture in deep navy and black tones"></div>
      <div class="cover-type">
        <h1 class="album-title">Garden of Silent Wells</h1>
        <p class="artist-name">Owen T.</p>
      </div>
    </section>
  </main>
</body>
</html>
```